Poem Handwritten by Veteran while in the jungle of Vietnam

My parents are celebrating their 50th wedding anniversary this year. I wanted to give them a very memorable gift. On my parents 2nd anniversary, my father was stationed in Vietnam. On that night he was in the jungle waiting till morning and wrote a poem to my mother using his pant leg as paper. I would like this poem to typographically designed to be framed and hung on the wall.

I have attached a picture of the poem below. It will need to be 11x14 when printed for framing. It would be great if there was background or artwork to make it more visually interesting, perhaps in a watercolor. My parents have a transitional style. I have attached some possible color schemes as well. Cool greens, blue, neutral grays, with hints of berries or highlights of yellow. These are just a guide, I would be open to your interpretations.

Thank you for your help. This will hopefully be a gift they will truly treasure as much as the poem itself.

Target Market(s)

My parents who are excited to be celebrating their 50th wedding anniversary. It should have a transitional, mature style.

Font styles to use
Serif
Script

Requirements
Must have
• The poem, typographically designed. There can be a mix of fonts, but legibility is critically important.
• Now that some designs have come through I wanted to give some more guidance of what I'm looking for. I want something that feels sophisticated and artistic.
Nice to have
• A background or art work, using the color schemes attached as a guide. I am really liking the designs that have a full color landscape artwork in the background. The fonts should be elegant and formal. I really like the romantic, muted colors. I had trouble finding similar projects online in the style I wanted until I cam across wedding invites. Those seem to be the most applicable. I've added pictures of some so you can get a sense of what I'm looking for. I am really liking the jungle foliage, starry skies or sunrises.
Should not have
• Cartoon caricatures, fonts that are too illegible when printed. I'm not liking anything whimsical. I don't like the very bright colors for this project.

```html
<!DOCTYPE html>
<html lang="en">
<head>
<meta charset="utf-8">
<title>Harold's Anniversary Poem</title>
<link rel="stylesheet" href="https://fonts.googleapis.com/css2?family=Libre+Baskerville:wght@400;700&family=Open+Sans:wght@400&display=swap">
<style>
  :root {
    --page-bg: #e4e4e4;
    --ink: #1f2b3c;
    --ink-soft: #3b4758;
    --rule: #5a6677;
    --note: #8c929a;
    --sky-top: #a7cbe6;
    --sky-mid: #c7d9e4;
    --haze: #b8c3c8;
    --glow: #dcb690;
    --hill: #6f7d88;
    --forest: #2f3c43;
    --night: #0b0d10;
  }
  * { margin: 0; padding: 0; box-sizing: border-box; }
  html, body { width: 1200px; height: 1200px; overflow: hidden; background: var(--page-bg); }
  .poster {
    position: absolute; left: 160px; top: 40px; width: 880px; height: 1120px; overflow: hidden;
  }
  .landscape {
    position: absolute; inset: 0;
    background:
      radial-gradient(ellipse 60% 9% at 42% 55%, rgba(240,190,130,0.75), rgba(240,190,130,0) 70%),
      linear-gradient(180deg, var(--sky-top) 0%, var(--sky-mid) 28%, var(--haze) 44%, var(--glow) 54%, var(--hill) 61%, var(--forest) 72%, #161b20 84%, var(--night) 100%);
  }
  .dateline {
    position: absolute; top: 38px; left: 21px; width: 818px;
    display: flex; align-items: center; gap: 10px;
    font-family: "Libre Baskerville", serif; font-size: 22px; color: var(--ink-soft);
  }
  .dateline .rule { flex: 1; height: 1px; background: var(--rule); position: relative; }
  .dateline .rule::after {
    content: ""; position: absolute; top: -3px; width: 7px; height: 7px; border-radius: 50%; background: var(--rule);
  }
  .dateline .rule.left::after { right: -2px; }
  .dateline .rule.right::after { left: -2px; }
  .title {
    position: absolute; top: 72px; left: 0; width: 100%; text-align: center;
    font-family: "Libre Baskerville", serif; font-weight: 700; font-size: 29px; color: var(--ink);
  }
  .poem-column {
    position: absolute; top: 136px; width: 300px; text-align: center;
    font-family: "Open Sans", sans-serif; font-size: 14px; line-height: 18.5px; color: var(--ink);
    white-space: nowrap;
  }
  .poem-column.left { left: 130px; }
  .poem-column.right { left: 434px; }
  .stanza { margin-bottom: 18px; }
  .footnote {
    position: absolute; left: 78px; top: 962px; width: 760px;
    font-family: "Libre Baskerville", serif; font-size: 15px; line-height: 18px; color: var(--note);
  }
</style>
</head>
<body>
<main class="poster">
  <div class="landscape" role="img" aria-label="Painted landscape at dawn: pale blue sky, warm sunrise glow over misty mountains, dark jungle foliage silhouettes below"></div>

  <header>
    <div class="dateline">
      <span class="rule left"></span>
      <span>20 JULY 1970, MONDAY, LZ PROFESSIONAL</span>
      <span class="rule right"></span>
    </div>
    <h1 class="title">HAROLD’S ANNIVERSARY POEM</h1>
  </header>

  <section class="poem-column left">
    <p class="stanza">Life’s journey began with a challenge,<br>It was heralded far and near.<br>The road led on forever,<br>Its completion was known to be dear.</p>
    <p class="stanza">From the garden of light it proceeded,<br>To the valley of shadows it led<br>Thorns and thistles adorned it,<br>Past abyss and crevice it sped.</p>
    <p class="stanza">The brave surged forward with courage,<br>The wise undaunted pressed on.<br>The mighty held high their banner,<br>We all awaited the dawn.</p>
    <p class="stanza">Though the pitfalls and hazards were many,<br>The pathway was clearly in view.<br>Straight and sure it glided,<br>Its course we knew to be true.</p>
    <p class="stanza">I knew you, Sweetheart, beforehand,<br>So precious and sweet were you.<br>Our moments of bliss were priceless,<br>Each day brought us joy anew.</p>
  </section>

  <section class="poem-column right">
    <p class="stanza">The call to progression beckoned,<br>At last I would have my chance<br>To clasp you to me forever,<br>And seal our divine romance.</p>
    <p class="stanza">I eagerly started the journey,<br>Though with sorrow, I left you behind.<br>With courage and faith I continued,<br>For I knew, that you later I’d find.</p>
    <p class="stanza">I diligently searched for you, Darling,<br>The roadway was both bleak and fair.<br>Though the years grew long in number,<br>I did not give up in despair.</p>
    <p class="stanza">At last in the distance I saw you,<br>So beautiful, lovely, and sweet !<br>Your attention I struggled to capture,<br>Your love I wrested to meet.</p>
    <p class="stanza">What rapture was mine in fulfillment,<br>As now together we stand.<br>To cherish and love each other,<br>While our plans and dreams expand.</p>
    <p class="stanza">I love you, Darling, forever,<br>My life you have made replete.<br>Our eternal mansion beckons,<br>Your love has made it complete.</p>
  </section>

  <footer class="footnote">
    <p>This poem was written during the dark of night while on guard duty at L3 Professional in Viet Nam. I was at the time a 2nd Lieutenant in the Infantry. The date was July 1970, our second anniversary.</p>
    <p>The orginal was penciled onto my fatigue uniform, arranging only the key rthyming words without light to see</p>
  </footer>
</main>
</body>
</html>
```